Personal Injury Billboard for a law frim

Our firm has a billboard we need art for. It will specifically for personal injury cases. The dimensions of art the billboard are 9 ft high 29 feet wide.

We want to highlight the terms, "Serious Injuries" and "Trusted. Local. Experienced." We want to incorporate the attached "Vantor Advocates" badge as well as our attached firm logo. We want the blue color scheme (see attached).

Maybe an image of an industrial plant in the background?

Font styles to use
Sans Serif

Colors

Designer to choose colors to be used in the design.

```html
<!DOCTYPE html>
<html lang="en">
<head>
<meta charset="utf-8">
<title>Halden Morrow Pike – Serious Injuries Billboard</title>
<link rel="stylesheet" href="https://fonts.googleapis.com/css2?family=Noto+Serif:wght@700&family=Roboto:wght@500;700;900&display=swap">
<style>
  :root {
    --page-bg: #e9edf2;
    --navy: #0b2a63;
    --royal: #1565c0;
    --sky-top: #a9c6e2;
    --sky-mid: #d6e3ee;
    --plant-grey: #9aa6b2;
    --white: #ffffff;
    --ink: #1b1b1b;
    --badge-dark: #3a3a3a;
    --badge-blue: #1565c0;
    --badge-orange: #f5a21b;
    --badge-red: #a31c2b;
  }
  * { box-sizing: border-box; margin: 0; padding: 0; }
  html, body { width: 1200px; height: 879px; overflow: hidden; background: var(--page-bg); }
  .billboard {
    position: absolute; left: 0; top: 253px;
    width: 1200px; height: 372px; overflow: hidden; background: var(--white);
  }
  .billboard__scene {
    position: absolute; inset: 0;
    background:
      linear-gradient(to bottom, rgba(255,255,255,0) 55%, rgba(154,166,178,0.55) 100%),
      linear-gradient(to bottom, var(--sky-top) 0%, var(--sky-mid) 60%, #c5ccd3 100%);
  }
  .billboard__panel { position: absolute; left: 0; top: 0; width: 440px; height: 372px; }
  .brand {
    position: absolute; left: 20px; top: 90px; width: 330px;
    display: flex; flex-direction: column; align-items: center;
    font-family: "Roboto", sans-serif;
  }
  .brand__mark { display: flex; align-items: center; gap: 12px; }
  .brand__square { width: 46px; height: 46px; background: var(--royal); }
  .brand__initials { font-weight: 900; font-size: 64px; color: var(--royal); letter-spacing: 6px; line-height: 1; }
  .brand__url { margin-top: 22px; font-size: 19px; font-weight: 500; color: var(--royal); text-decoration: underline; }
  .brand__name { margin-top: 6px; font-size: 21px; font-weight: 700; color: var(--ink); letter-spacing: 0.5px; }
  .brand__tag {
    margin-top: 4px; font-size: 11px; font-weight: 700; color: var(--ink); letter-spacing: 2px;
    display: flex; align-items: center; gap: 8px;
  }
  .brand__tag::before, .brand__tag::after { content: ""; width: 110px; height: 2px; background: var(--ink); }
  .headline {
    position: absolute; right: 60px; top: 26px; width: 620px;
    font-family: "Noto Serif", serif; font-weight: 700; color: var(--navy);
    font-size: 58px; line-height: 1.1; text-align: center;
  }
  .awards { position: absolute; left: 640px; top: 264px; display: flex; gap: 8px; }
  .award {
    width: 116px; height: 98px; border: 2px solid #bbb; border-radius: 6px;
    background: var(--white); display: flex; flex-direction: column; justify-content: flex-end; overflow: hidden;
  }
  .award__band { height: 26px; }
  .award--selected .award__band { background: var(--badge-dark); }
  .award--blue { background: var(--badge-blue); }
  .award--blue .award__band { background: var(--white); }
  .award--top .award__band { height: 52px; background: var(--badge-orange); border-bottom: 22px solid var(--white); }
  .award--years .award__band { height: 54px; background: var(--badge-red); border-bottom: 28px solid var(--white); }
</style>
</head>
<body>
  <section class="billboard" aria-label="Personal injury billboard">
    <div class="billboard__scene" role="img" aria-label="Industrial power plant with smokestacks and cooling towers under a pale blue sky"></div>

    <svg class="billboard__panel" viewBox="0 0 440 372" aria-hidden="true">
      <path d="M0 0 H282 Q 405 150 388 372 H0 Z" fill="#ffffff"/>
      <path d="M282 0 H302 Q 430 150 414 372 H388 Q 405 150 282 0 Z" fill="#1565c0"/>
    </svg>

    <div class="brand">
      <div class="brand__mark">
        <span class="brand__square"></span>
        <span class="brand__initials">HMP</span>
      </div>
      <span class="brand__url">www.hmp-law.com</span>
      <span class="brand__name">HALDEN MORROW PIKE</span>
      <span class="brand__tag">ATTORNEYS</span>
    </div>

    <h1 class="headline">Serious Injuries<br>Trusted. Local.<br>Experienced</h1>

    <div class="awards" aria-label="Vantor Advocates recognitions">
      <div class="award award--selected"><span class="award__band"></span></div>
      <div class="award award--blue"><span class="award__band"></span></div>
      <div class="award award--top"><span class="award__band"></span></div>
      <div class="award award--years"><span class="award__band"></span></div>
    </div>
  </section>
</body>
</html>
```